Design single page website for fitness center

Object : Design single page website for fitness centre
Instructions:
1) The design should as minimalist as possible
2)Use icons for contact info
3)Leave space for content regarding
SERVICES, PACKAGES, BILLING ( PAYMENT PORTALS)

```html
<!DOCTYPE html>
<html lang="en">
<head>
<meta charset="utf-8">
<title>Fitness</title>
<link rel="stylesheet" href="https://fonts.googleapis.com/css2?family=Arimo:wght@400;700&display=swap">
<style>
  :root {
    --ink-white: #ffffff;
    --ink-dark: #2b2b2b;
    --hero-deep: #1f2421;
    --hero-mid: #3c4441;
    --hero-light: #6d7672;
    --hairline: rgba(255, 255, 255, 0.22);
  }
  * { box-sizing: border-box; margin: 0; padding: 0; }
  html, body {
    width: 1200px;
    height: 583px;
    overflow: hidden;
    font-family: "Arimo", Arial, sans-serif;
    background: var(--hero-deep);
  }
  .hero {
    position: relative;
    width: 1200px;
    height: 583px;
    overflow: hidden;
  }
  .hero__photo {
    position: absolute;
    inset: 0;
    background:
      radial-gradient(ellipse at 80% 55%, rgba(140, 150, 146, 0.45), transparent 60%),
      radial-gradient(ellipse at 25% 70%, rgba(120, 110, 100, 0.35), transparent 55%),
      linear-gradient(180deg, var(--hero-mid) 0%, var(--hero-deep) 100%);
  }
  .hero__shade {
    position: absolute;
    inset: 0;
    background: rgba(0, 0, 0, 0.28);
  }
  .topbar {
    position: absolute;
    top: 0;
    left: 0;
    right: 0;
    height: 52px;
    border-bottom: 1px solid var(--hairline);
    display: flex;
    align-items: center;
    justify-content: center;
    gap: 6px;
    color: var(--ink-white);
    font-size: 15px;
  }
  .topbar__icon { width: 11px; height: 15px; }
  .hero__content {
    position: absolute;
    top: 200px;
    left: 0;
    right: 0;
    display: flex;
    flex-direction: column;
    align-items: center;
    color: var(--ink-white);
    padding-left: 40px;
  }
  .hero__title {
    font-weight: 400;
    font-size: 142px;
    line-height: 1;
    letter-spacing: 1px;
  }
  .hero__rule {
    width: 166px;
    height: 3px;
    background: var(--ink-white);
    margin-top: 40px;
  }
  .hero__tagline {
    margin-top: 26px;
    font-weight: 700;
    font-size: 15px;
    letter-spacing: 0.6px;
  }
  .hero__button {
    margin-top: 48px;
    width: 207px;
    height: 52px;
    border-radius: 26px;
    background: var(--ink-white);
    color: var(--ink-dark);
    font-size: 17px;
    display: flex;
    align-items: center;
    justify-content: center;
    text-decoration: none;
  }
</style>
</head>
<body>
  <section class="hero">
    <div class="hero__photo" role="img" aria-label="Photo of a group fitness class stretching in a bright studio with mirrors and large windows"></div>
    <div class="hero__shade"></div>

    <header class="topbar">
      <svg class="topbar__icon" viewBox="0 0 11 15" aria-hidden="true">
        <path d="M5.5 0C2.5 0 0 2.4 0 5.4 0 9.4 5.5 15 5.5 15S11 9.4 11 5.4C11 2.4 8.5 0 5.5 0Zm0 7.6a2.2 2.2 0 1 1 0-4.4 2.2 2.2 0 0 1 0 4.4Z" fill="#fff"/>
      </svg>
      <span class="topbar__address">Harbor Ln,Canada,Maple 20418, Westbrook City</span>
    </header>

    <div class="hero__content">
      <h1 class="hero__title">Fitness</h1>
      <div class="hero__rule"></div>
      <p class="hero__tagline">LOREM IPSUM DOLOR SIT AMET</p>
      <a class="hero__button" href="#">Read More</a>
    </div>
  </section>
</body>
</html>
```